Lanternleaf - Fresh Asian Cuisine Menu

We need to redo our menu to include pictures of food items. Our restaurant is vibrant, trendy, upscale Chinese cuisine

Requirements
Must have
• Must fit on 8.5x11 paper. We can remove the About Us section if needed but menu cannot be more than 6 pages total. Must include pictures of menu items

```html
<!DOCTYPE html>
<html lang="en">
<head>
<meta charset="utf-8">
<title>Lanternleaf – Lunch Menu</title>
<link rel="stylesheet" href="https://fonts.googleapis.com/css2?family=Cinzel:wght@600&family=Fira+Sans:wght@600&family=Fira+Sans+Condensed:wght@400&family=Great+Vibes&display=swap">
<style>
  :root {
    --backdrop: #ece6e4;
    --paper: #ffffff;
    --paper-tint: #f8f4f3;
    --red-deep: #7d1518;
    --red: #b3121c;
    --red-bright: #c8161f;
    --photo-warm: #c9813f;
    --photo-deep: #8a3a1c;
  }
  html, body {
    margin: 0;
    width: 1200px;
    height: 1200px;
    overflow: hidden;
    background: var(--backdrop);
  }
  .menu-page {
    position: absolute;
    left: 202px;
    top: 70px;
    width: 997px;
    height: 1290px;
    background: var(--paper);
    transform: scale(0.8);
    transform-origin: top left;
    color: var(--red);
    box-shadow: 0 4px 18px rgba(60, 10, 10, 0.18);
  }
  .pattern-field {
    position: absolute;
    left: 0; right: 0;
    top: 145px;
    bottom: 42px;
    background: linear-gradient(180deg, var(--paper-tint), #f5f0ef);
  }
  .corner-ornament {
    position: absolute;
    top: 11px;
    width: 112px;
    height: 84px;
    background: linear-gradient(135deg, #f3dcdc, #e9c3c4);
  }
  .corner-ornament--left { left: 20px; }
  .corner-ornament--right { right: 20px; }

  .brand {
    position: absolute;
    left: 236px;
    top: 38px;
    width: 100px;
    display: flex;
    flex-direction: column;
    align-items: center;
    gap: 4px;
  }
  .brand__dot {
    width: 70px; height: 70px;
    border-radius: 50%;
    background: var(--red-deep);
  }
  .brand__name {
    font-family: "Fira Sans", sans-serif;
    font-weight: 600;
    font-size: 13px;
    color: var(--red-deep);
  }
  .menu-title {
    position: absolute;
    left: 341px;
    top: 34px;
    margin: 0;
    font-family: "Cinzel", serif;
    font-weight: 600;
    font-size: 52px;
    line-height: 1;
    color: var(--red-deep);
    transform: scaleY(1.3);
    transform-origin: top left;
    white-space: nowrap;
  }
  .menu-hours {
    position: absolute;
    left: 341px;
    top: 96px;
    margin: 0;
    font-family: "Great Vibes", cursive;
    font-size: 25px;
    color: var(--red-deep);
    white-space: nowrap;
  }

  .dish {
    position: absolute;
    width: 424px;
  }
  .dish--left { left: 63px; }
  .dish--right { left: 526px; width: 422px; }
  .dish__head {
    display: flex;
    align-items: flex-start;
  }
  .dish__name {
    margin: 0;
    font-family: "Fira Sans", sans-serif;
    font-weight: 600;
    font-size: 23px;
    line-height: 26px;
    color: var(--red-deep);
    letter-spacing: 0.3px;
    white-space: nowrap;
  }
  .dish__name--wrap { max-width: 300px; white-space: normal; }
  .dish__leader {
    flex: 1;
    height: 18px;
    margin: 0 10px 0 22px;
    border-bottom: 2px dotted var(--red);
  }
  .dish__price {
    font-family: "Fira Sans", sans-serif;
    font-weight: 600;
    font-size: 23px;
    line-height: 26px;
    color: var(--red);
  }
  .dish__desc {
    margin: 3px 0 0;
    max-width: 250px;
    font-family: "Fira Sans Condensed", sans-serif;
    font-size: 13.5px;
    line-height: 16.5px;
    color: var(--red-bright);
  }
  .dish__photo {
    position: absolute;
    right: 0;
    top: 33px;
    width: 74px;
    height: 46px;
    border-radius: 4px;
    background: radial-gradient(circle at 45% 45%, var(--photo-warm), var(--photo-deep));
  }
  .fret-band {
    position: absolute;
    left: 0; right: 0;
    bottom: 12px;
    height: 32px;
    border-top: 3px solid var(--red);
    border-bottom: 3px solid var(--red);
    background: linear-gradient(180deg, #d44a4f, #c0272d);
    box-sizing: border-box;
  }
</style>
</head>
<body>
<main class="menu-page">
  <div class="pattern-field" role="img" aria-label="Subtle repeating wave pattern background"></div>
  <div class="corner-ornament corner-ornament--left" role="img" aria-label="Red fretwork corner ornament with flower motif"></div>
  <div class="corner-ornament corner-ornament--right" role="img" aria-label="Red fretwork corner ornament with star motif"></div>

  <div class="brand">
    <span class="brand__dot"></span>
    <span class="brand__name">Lanternleaf</span>
  </div>
  <h1 class="menu-title">LUNCH MENU</h1>
  <p class="menu-hours">available Monday – Friday from 11 am to 3pm</p>

  <!-- Left column -->
  <article class="dish dish--left" style="top:168px">
    <div class="dish__head"><h2 class="dish__name">Kung Pao Chicken</h2><span class="dish__leader"></span><span class="dish__price">$10</span></div>
    <p class="dish__desc" style="max-width:240px">Chicken sautéed with roasted peanuts and dry red chili in Kung Pao sauce</p>
    <div class="dish__photo" role="img" aria-label="Photo of Kung Pao Chicken"></div>
  </article>
  <article class="dish dish--left" style="top:261px">
    <div class="dish__head"><h2 class="dish__name">Orange Chicken</h2><span class="dish__leader"></span><span class="dish__price">$10</span></div>
    <p class="dish__desc" style="max-width:255px">Battered-fried chicken breast with dried chili peppers and stir fried in a tangy orange flavored sauce</p>
    <div class="dish__photo" role="img" aria-label="Photo of Orange Chicken"></div>
  </article>
  <article class="dish dish--left" style="top:361px">
    <div class="dish__head"><h2 class="dish__name">Crispy Spicy Chicken</h2><span class="dish__leader"></span><span class="dish__price">$11</span></div>
    <p class="dish__desc" style="max-width:285px">Crispy-diced chicken with Sichuan peppers, garlic, scallions and red and green bell peppers</p>
    <div class="dish__photo" role="img" aria-label="Photo of Crispy Spicy Chicken"></div>
  </article>
  <article class="dish dish--left" style="top:468px">
    <div class="dish__head"><h2 class="dish__name">General Tso’s Chicken</h2><span class="dish__leader"></span><span class="dish__price">$10</span></div>
    <p class="dish__desc" style="max-width:245px">Battered-fried chicken breast, stir fried in a sweet &amp; tangy chili sauce with chili peppers</p>
    <div class="dish__photo" role="img" aria-label="Photo of General Tso’s Chicken"></div>
  </article>
  <article class="dish dish--left" style="top:549px">
    <div class="dish__head"><h2 class="dish__name dish__name--wrap">Shredded Chicken in Spicy Garlic Sauce</h2><span class="dish__leader"></span><span class="dish__price">$11</span></div>
    <p class="dish__desc" style="max-width:300px">Battered-fried chicken breast with dried chili peppers and stir fried in a tangy orange flavored sauce</p>
    <div class="dish__photo" role="img" aria-label="Photo of Shredded Chicken in Spicy Garlic Sauce" style="top:58px"></div>
  </article>
  <article class="dish dish--left" style="top:661px">
    <div class="dish__head"><h2 class="dish__name">Sweet &amp; Sour Chicken</h2><span class="dish__leader"></span><span class="dish__price">$10</span></div>
    <p class="dish__desc" style="max-width:285px">Crispy Chicken with green bell peppers, onions and pineapple glazed in a homemade sweet and sour marinade</p>
    <div class="dish__photo" role="img" aria-label="Photo of Sweet and Sour Chicken"></div>
  </article>
  <article class="dish dish--left" style="top:762px">
    <div class="dish__head"><h2 class="dish__name">Orange Chicken</h2><span class="dish__leader"></span><span class="dish__price">$11</span></div>
    <p class="dish__desc" style="max-width:230px">Battered-fried chicken breast with dried chili peppers and stir fried in a tangy orange flavored sauce</p>
    <div class="dish__photo" role="img" aria-label="Photo of Orange Chicken"></div>
  </article>
  <article class="dish dish--left" style="top:862px">
    <div class="dish__head"><h2 class="dish__name">Oyster Beef</h2><span class="dish__leader"></span><span class="dish__price">$12</span></div>
    <p class="dish__desc" style="max-width:250px">Tender cuts of steak wok fried with onions and marinated in a homemade oyster sauce</p>
    <div class="dish__photo" role="img" aria-label="Photo of Oyster Beef"></div>
  </article>
  <article class="dish dish--left" style="top:962px">
    <div class="dish__head"><h2 class="dish__name">Black Pepper</h2><span class="dish__leader"></span><span class="dish__price">$11</span></div>
    <p class="dish__desc" style="max-width:265px">Black Pepper Steak Tender cuts of steak mixed with onions and red and green bell peppers</p>
    <div class="dish__photo" role="img" aria-label="Photo of Black Pepper Steak"></div>
  </article>
  <article class="dish dish--left" style="top:1070px">
    <div class="dish__head"><h2 class="dish__name">Dancing Pork</h2><span class="dish__leader"></span><span class="dish__price">$11</span></div>
    <p class="dish__desc" style="max-width:235px">Dancing Pork Belly Braised Pork Belly on sizzling rice cracker</p>
    <div class="dish__photo" role="img" aria-label="Photo of Dancing Pork"></div>
  </article>
  <article class="dish dish--left" style="top:1162px">
    <div class="dish__head"><h2 class="dish__name">Twice Cooked</h2><span class="dish__leader"></span><span class="dish__price">$11</span></div>
    <p class="dish__desc" style="max-width:255px">Twice Cooked Pork Stir fried Pork Belly slices with leek and fermented black beans</p>
    <div class="dish__photo" role="img" aria-label="Photo of Twice Cooked Pork"></div>
  </article>

  <!-- Right column -->
  <article class="dish dish--right" style="top:164px">
    <div class="dish__head"><h2 class="dish__name">Lemon Peel Shrimp</h2><span class="dish__leader"></span><span class="dish__price">$12</span></div>
    <p class="dish__desc" style="max-width:240px">Shrimp with fresh lemons in a sweet lemon sauce on a bed of shredded lettuce</p>
    <div class="dish__photo" role="img" aria-label="Photo of Lemon Peel Shrimp"></div>
  </article>
  <article class="dish dish--right" style="top:257px">
    <div class="dish__head"><h2 class="dish__name">Rice Wine Fish</h2><span class="dish__leader"></span><span class="dish__price">$11</span></div>
    <p class="dish__desc" style="max-width:225px">White fish filet with rice wine mixed with onions, peas and carrots</p>
    <div class="dish__photo" role="img" aria-label="Photo of Rice Wine Fish"></div>
  </article>
  <article class="dish dish--right" style="top:357px">
    <div class="dish__head"><h2 class="dish__name">Lanternleaf Fried Rice</h2><span class="dish__leader"></span><span class="dish__price">$10</span></div>
    <p class="dish__desc" style="max-width:240px">Shrimp, chicken, and beef, farm fresh eggs, onions, and scallions</p>
    <div class="dish__photo" role="img" aria-label="Photo of Lanternleaf Fried Rice"></div>
  </article>
  <article class="dish dish--right" style="top:465px">
    <div class="dish__head"><h2 class="dish__name">Vegetarian White Fried Rice</h2><span class="dish__leader"></span><span class="dish__price">$9</span></div>
    <p class="dish__desc">Mixed vegetables with white rice</p>
    <div class="dish__photo" role="img" aria-label="Photo of Vegetarian White Fried Rice"></div>
  </article>
  <article class="dish dish--right" style="top:549px">
    <div class="dish__head"><h2 class="dish__name">Lanternleaf Lo Mein</h2><span class="dish__leader"></span><span class="dish__price">$10</span></div>
    <p class="dish__desc" style="max-width:240px">Shrimp, chicken, and beef, farm fresh eggs, onions, and scallions</p>
    <div class="dish__photo" role="img" aria-label="Photo of Lanternleaf Lo Mein"></div>
  </article>
  <article class="dish dish--right" style="top:658px">
    <div class="dish__head"><h2 class="dish__name">Vegetarian Lo Mein</h2><span class="dish__leader"></span><span class="dish__price">$9</span></div>
    <p class="dish__desc">Mixed vegetables with lo mein noodles</p>
    <div class="dish__photo" role="img" aria-label="Photo of Vegetarian Lo Mein"></div>
  </article>
  <article class="dish dish--right" style="top:758px">
    <div class="dish__head"><h2 class="dish__name">Mapo Tofu</h2><span class="dish__leader"></span><span class="dish__price">$9</span></div>
    <p class="dish__desc" style="max-width:225px">Battered-fried chicken breast with dried chili peppers and stir fried in a tangy orange flavored sauce</p>
    <div class="dish__photo" role="img" aria-label="Photo of Mapo Tofu"></div>
  </article>
  <article class="dish dish--right" style="top:864px">
    <div class="dish__head"><h2 class="dish__name">Spicy Garlic Eggplant</h2><span class="dish__leader"></span><span class="dish__price">$10</span></div>
    <p class="dish__desc" style="max-width:215px">Chinese eggplant in spicy garlic sauce garnished with scallions</p>
    <div class="dish__photo" role="img" aria-label="Photo of Spicy Garlic Eggplant"></div>
  </article>
  <article class="dish dish--right" style="top:963px">
    <div class="dish__head"><h2 class="dish__name">Stir Fried Eggplant</h2><span class="dish__leader"></span><span class="dish__price">$10</span></div>
    <p class="dish__desc">Chinese eggplant with sautéed green beans</p>
    <div class="dish__photo" role="img" aria-label="Photo of Stir Fried Eggplant"></div>
  </article>
  <article class="dish dish--right" style="top:1070px">
    <div class="dish__head"><h2 class="dish__name">Shiitake Baby Bok</h2><span class="dish__leader"></span><span class="dish__price">$10</span></div>
    <p class="dish__desc" style="max-width:210px">Sautéed baby bok-choy with Shiitake mushrooms in brown sauce</p>
    <div class="dish__photo" role="img" aria-label="Photo of Shiitake Baby Bok Choy"></div>
  </article>

  <div class="fret-band" role="img" aria-label="Red Chinese fret pattern border"></div>
</main>
</body>
</html>
```